Refresh of a rather different IT outfit website

Our web site is starting to show it's age. You can see the existing site here: www.plumbcorner.net. As a growing company we want to come across as a dynamic collection of IT experts.

We want to update the design so are open to any colour palette and look, but want to retain our current table logo. We use the logo on our business cards but with a white background - see the attached file, so you don't need to keep the brown or the green.

The design should consider the range of browsers that will be looking at the site - so please show how it will look on a wide screen laptop and a 768x1024 tablet.

We want to add some pages about our team and their skills, probably with photos of each person on the team.

This is an uncoded project - the PSD files of the design is required, not coding.
Updates

Thanks everyone for the submissions so far.  It's a holiday day in the UK today but we will get some feedback on the designs so far out to you.

Target Market(s)

Architects and other creative types looking for IT support

Industry/Entity Type

Business

Font styles to use
Serif
Sans Serif

Requirements
Must have
• Must look good on a laptop and an iPad.

```html
<!DOCTYPE html>
<html lang="en">
<head>
<meta charset="utf-8">
<title>plumbcorner – Serious IT Support for Business</title>
<link rel="stylesheet" href="https://fonts.googleapis.com/css2?family=Oxygen:wght@300;400;700&family=Open+Sans:wght@400;600&display=swap">
<style>
  :root {
    --plum: #8c0b55;
    --plum-dark: #6e0342;
    --plum-bright: #a8106c;
    --gold: #e2b705;
    --gold-dark: #cf9f00;
    --ink: #333333;
    --body: #6b6b6b;
    --muted: #7d7d7d;
    --line: #e8e8e8;
    --footer: #f4f4f4;
    --white: #ffffff;
  }
  * { box-sizing: border-box; margin: 0; padding: 0; }
  html, body { width: 1116px; height: 1200px; overflow: hidden; background: var(--white); }
  body { position: relative; font-family: "Open Sans", Arial, sans-serif; color: var(--body); }

  .brand { position: absolute; left: 128px; top: 40px; display: flex; align-items: center; gap: 18px; }
  .brand-mark { width: 36px; height: 36px; background: var(--gold); }
  .brand-name { font-family: "Oxygen", Arial, sans-serif; font-weight: 700; font-size: 40px; color: var(--plum); letter-spacing: 0.5px; line-height: 1; }

  .main-nav { position: absolute; left: 130px; top: 106px; width: 851px; height: 46px; display: flex;
    background: linear-gradient(#e6be08, var(--gold-dark)); }
  .main-nav a { flex: auto; display: flex; align-items: center; justify-content: center; color: var(--white);
    font-family: "Oxygen", Arial, sans-serif; font-size: 15px; text-decoration: none; border-right: 1px solid #c99a00; box-shadow: 1px 0 0 #eccb3a; }
  .main-nav a:last-child { border-right: 0; box-shadow: none; }

  .hero { position: absolute; left: 0; top: 152px; width: 1116px; height: 354px;
    background: linear-gradient(90deg, #8a0650, #9a0a5c 50%, #7c0347); }
  .hero-stage { position: absolute; left: 130px; top: 0; width: 856px; height: 354px;
    background: radial-gradient(ellipse at 70% 30%, #b4147a, #950a5c 55%, #780244); }
  .hero-photo { position: absolute; left: 506px; top: 10px; width: 250px; height: 344px;
    background: linear-gradient(#d9c6bf, #f4f1f2 45%, #e9e6e8); border-radius: 110px 110px 0 0; }
  .hero-copy { position: absolute; left: 61px; top: 92px; width: 420px; color: var(--white); }
  .hero-copy h1 { font-family: "Oxygen", Arial, sans-serif; font-weight: 400; font-size: 38px; line-height: 44px; }
  .hero-copy p { margin-top: 14px; font-size: 11.5px; line-height: 18.5px; color: #f3dceb; }
  .hero-dots { display: flex; gap: 4px; margin-top: 17px; }
  .hero-dots span { width: 10px; height: 10px; border-radius: 50%; background: #c58aaf; }

  .services { position: absolute; left: 130px; top: 525px; width: 856px; height: 235px; display: flex; }
  .service { border-right: 1px solid #eeeeee; border-left: 1px solid #f2f2f2; text-align: center; position: relative; }
  .service svg { display: block; margin: 18px auto 0; }
  .service h2 { font-family: "Oxygen", Arial, sans-serif; font-weight: 400; font-size: 19px; line-height: 21px; color: var(--ink); margin-top: 16px; }
  .service p { font-size: 10.5px; line-height: 17.5px; color: var(--muted); margin: 6px auto 0; width: 186px; }
  .btn { position: absolute; left: 50%; top: 188px; transform: translateX(-50%); width: 80px; height: 24px;
    background: linear-gradient(#e8bf0c, var(--gold-dark)); color: var(--white); font-size: 11px; line-height: 24px;
    text-decoration: none; border-radius: 2px; }

  .divider { position: absolute; left: 120px; top: 776px; width: 876px; height: 1px; background: var(--line);
    box-shadow: 0 10px 20px rgba(0,0,0,0.03); }

  .about { position: absolute; left: 130px; top: 818px; width: 442px; }
  .about h2 { font-family: "Oxygen", Arial, sans-serif; font-weight: 300; font-size: 24px; color: var(--plum); margin-left: 2px; }
  .about p { font-size: 11px; line-height: 18.5px; margin-top: 14px; }
  .about p + p { margin-top: 12px; }

  .news { position: absolute; left: 624px; top: 824px; width: 380px; }
  .news h2 { font-family: "Oxygen", Arial, sans-serif; font-weight: 300; font-size: 23px; color: var(--ink); }
  .post { display: flex; gap: 12px; margin-top: 14px; }
  .post + .post { margin-top: 28px; }
  .post-thumb { flex: none; width: 69px; height: 52px; }
  .post-thumb.first { background: linear-gradient(#cdd4db, #8c98a4); }
  .post-thumb.second { background: linear-gradient(90deg, #6fa9bf, #e8d8c4); }
  .post h3 { font-family: "Oxygen", Arial, sans-serif; font-weight: 700; font-size: 14px; color: var(--plum); margin-top: -2px; }
  .post p { font-size: 11.5px; line-height: 17px; margin-top: 3px; }

  .site-footer { position: absolute; left: 0; top: 1083px; width: 1116px; height: 117px; background: var(--footer); }
  .footer-nav { position: absolute; left: 128px; top: 30px; font-size: 13px; color: #555; letter-spacing: 0.2px; }
  .footer-nav a { color: #555; text-decoration: none; }
  .footer-nav span { margin: 0 8px; }
  .copyright { position: absolute; left: 130px; top: 60px; font-size: 11px; color: #777; }
  .social { position: absolute; left: 869px; top: 27px; display: flex; gap: 3px; }
  .social span { width: 26px; height: 26px; border-radius: 50%; background: #111; }
</style>
</head>
<body>
  <header>
    <div class="brand"><span class="brand-mark"></span><span class="brand-name">plumbcorner</span></div>
    <nav class="main-nav">
      <a href="#">Home</a><a href="#">About Us</a><a href="#">What we do</a><a href="#">News Blog</a><a href="#">Articles</a><a href="#">Clients</a><a href="#">Partners</a><a href="#">Support</a><a href="#">Contact</a>
    </nav>
  </header>

  <section class="hero">
    <div class="hero-stage" role="img" aria-label="Magenta background with a faint pattern of binary digits">
      <div class="hero-photo" role="img" aria-label="Photo of a smiling support agent wearing a headset, arms folded"></div>
      <div class="hero-copy">
        <h1>Serious IT Support<br>for Business</h1>
        <p>Etiam eu urna Sed porta Suspendisse quam leo molestie sed luctus quis feugiat in pede Fusce tellus Sed metus augue convallis et vehicula</p>
        <div class="hero-dots"><span></span><span></span><span></span><span></span></div>
      </div>
    </div>
  </section>

  <section class="services">
    <article class="service" style="width:213px">
      <svg width="86" height="62" viewBox="0 0 86 62" fill="none" stroke="#8c0b55" stroke-width="6" stroke-linejoin="round">
        <path d="M20 56 H12 A10 10 0 0 1 10 36 A14 14 0 0 1 30 22 A20 20 0 0 1 66 24 A14 14 0 0 1 74 56 H64"/>
        <path d="M43 60 V36 M32 40 L43 28 L54 40" fill="#8c0b55"/>
      </svg>
      <h2>Cloud Computing</h2>
      <p>Phasellus felis dolor scelerisque a tempus eget, lobortis id, libero Donec scelerisque leo ac</p>
      <a class="btn" href="#">Read More</a>
    </article>
    <article class="service" style="width:209px">
      <svg width="86" height="68" viewBox="0 0 86 68" fill="none" stroke="#8c0b55" stroke-width="5">
        <circle cx="38" cy="20" r="10"/><circle cx="38" cy="20" r="15" stroke-dasharray="5 4" stroke-width="6"/>
        <circle cx="14" cy="42" r="7" stroke-dasharray="4 3" stroke-width="5"/>
        <path d="M40 38 H74 V62 H30"/><path d="M26 65 H82" stroke-width="4"/>
      </svg>
      <h2>IT Support &amp;<br>Management</h2>
      <p>Phasellus felis dolor scelerisque a tempus eget lobortis id, libero</p>
      <a class="btn" href="#">Read More</a>
    </article>
    <article class="service" style="width:226px">
      <svg width="76" height="66" viewBox="0 0 76 66" fill="none" stroke="#8c0b55" stroke-width="5">
        <rect x="3" y="3" width="70" height="46" rx="2"/>
        <path d="M14 38 L28 26 L38 33 L60 14" stroke-width="2.5"/>
        <path d="M38 49 V58 M22 61 H54" stroke-width="6"/>
      </svg>
      <h2>Virtualisation</h2>
      <p>Phasellus felis dolor scelerisque a tempus eget, lobortis id, libero Donec scelerisque leo ac</p>
      <a class="btn" href="#">Read More</a>
    </article>
    <article class="service" style="width:208px">
      <svg width="86" height="66" viewBox="0 0 86 66">
        <path d="M20 62 A16 16 0 0 1 16 32 A16 16 0 0 1 34 14 A20 20 0 0 1 66 22 A18 18 0 0 1 68 62 Z" fill="#8c0b55"/>
        <circle cx="38" cy="40" r="9" fill="none" stroke="#fff" stroke-width="5" stroke-dasharray="4 3"/>
        <circle cx="56" cy="30" r="6" fill="none" stroke="#fff" stroke-width="4" stroke-dasharray="3 3"/>
        <circle cx="56" cy="50" r="5" fill="none" stroke="#fff" stroke-width="4" stroke-dasharray="3 3"/>
      </svg>
      <h2>CAD Services</h2>
      <p>Phasellus felis dolor scelerisque a tempus eget, lobortis id, libero Donec scelerisque leo ac</p>
      <a class="btn" href="#">Read More</a>
    </article>
  </section>

  <div class="divider"></div>

  <section class="about">
    <h2>About Our Company</h2>
    <p>Aliquam nec erat at purus cursus interdum Vestibulum ligula augue bibendum accum-san vestibulum ut commodo a mi Morbi ornare gravida elit Integer congue augue et malesuada iaculis ipsum dui aliquet felis at cursus magna nisl nec elit</p>
    <p>Vestibulum gravida Praesent elementum elit at tellus Malesuada nec ultricies sit amet porttitor mattis enim In massa libero interdum nec interdum vel blandit sed nulla In ullamcorper est eget tempor cursus neque mi consectetuer Donec dictum lectus non odio Cras a ante vitae enim iaculis aliquam Mauris nunc quam venenatis nec euismod sit amet egestas placerat est Pellentesque habitant morbi tristique</p>
  </section>

  <section class="news">
    <h2>News &amp; Blog</h2>
    <article class="post">
      <div class="post-thumb first" role="img" aria-label="Photo of a man in a white shirt at a desk"></div>
      <div><h3>Blog post tittle</h3><p>Phasellus felis dolor scelerisque a tempus eget, lobortis id libero Donec scelerisque leo ac risus</p></div>
    </article>
    <article class="post">
      <div class="post-thumb second" role="img" aria-label="Photo of a woman wearing a headset in an office"></div>
      <div><h3>Blog post tittle</h3><p>Phasellus felis dolor scelerisque a tempus eget, lobortis id libero Donec scelerisque leo ac risus</p></div>
    </article>
  </section>

  <footer class="site-footer">
    <nav class="footer-nav">
      <a href="#">HOME</a><span>|</span><a href="#">ABOUT US</a><span>|</span><a href="#">WHAT WE DO</a><span>|</span><a href="#">NEWS BLOG</a><span>|</span><a href="#">ARTICLES</a><span>|</span><a href="#">CLIENTS</a><span>|</span><a href="#">SUPPORT</a><span>|</span><a href="#">CONTACT</a>
    </nav>
    <p class="copyright">© 2014 Company Name.&nbsp; All right reserved.&nbsp; Term of Use</p>
    <div class="social" aria-label="Social links"><span></span><span></span><span></span><span></span></div>
  </footer>
</body>
</html>
```